International MultiIndustry Team Coaching Site

Hello Designers,
We need a redesign of the pages attached.
The design must be engaging and modern, with a focus on the user experience, particularly for the "observations" page. Because this is the main page of the website. It is to be used on a 10'' tablet or desktop, to record observations on the fly, so it must be intuitive and efficient.
The positioning of the metrics and observations and etc, are just a reference. you can switch it up if you feel there is a better way (PLEASE DO ;) ).

There are many categories (color coded with borders in the example hpt_6_observations.jpg) and observation metrics within each category. This is the Key page, because it is the One with the most interactions.

The user should know when it has selected a category (there should be some visual hint) and the different metric widgets should be accounted for.
There are 3: The time widget at the end, numerical widgets (recording more or less numbers), and boolean ones (selected or not).

For the numerical widgets, we show plus and minus characters, but you can change this, being creative, keeping in mind that it must work well on a mobile device and desktop, and must be intuitive and quick.

Set your creativity free with the login screen , home screen, categories secret, events screen, journaling and observations screen .

We would like the site/mobile version to have a very modern look. Something that would be found in very popular and user friendly apps.

***** The events, journaling, category and home screens are getting 2 much attention , please focus also on the observations screen *******
Imagine you are a psychologist tasked with observing the behaviour of teenagers during group work. And you have a tablet on which to record what you observe. Now imagine you need to observe during 3 classes: Biology, Math, Physics (these are events). For each class (event) you will have to record observations in 3 categories: Social Interaction, Leadership, Communication (these are categories).
Example of the metrics (these are observations) for Leadership:
" the teenager direct other colleagues" (boolean widget),
"the teenager speaks more than everyone else" (boolean widget)
"the teenager interrupts colleagues speaking" (number widget)
"the work took hh:mm" (time widget)

The observations screen can have any shape and form you think of. It doesn't need to be that single column with yes and nos, or that double column with the squared cards.
thank you.

Hope that was useful intel :)
Available for any questions you might have.
Good luck :)

Enterprise teams

5+ page

Sans Serif

• Modern design

```html
<!DOCTYPE html>
<html lang="en">
<head>
<meta charset="utf-8">
<title>Teamlens – Team Coaching Screens</title>
<link href="https://fonts.googleapis.com/css2?family=Inter:wght@400;500;600;700&display=swap" rel="stylesheet">
<style>
:root{
  --blue:#3b9ad9;
  --blue-dark:#2a7fbf;
  --blue-soft:#e6f1fa;
  --ink:#2b2f36;
  --muted:#8a9099;
  --line:#dfe3e8;
  --bg:#f4f5f7;
  --white:#ffffff;
}
*{box-sizing:border-box;margin:0;padding:0}
html,body{width:1200px;height:3564px;overflow:hidden}
body{background:var(--bg);font-family:"Inter",sans-serif;color:var(--ink);position:relative}

/* style sheet header */
.sheet-head{position:absolute;top:70px;left:230px;width:740px;height:110px;display:flex;align-items:center}
.brand{display:flex;align-items:center;gap:12px;font-weight:700;font-size:40px;color:var(--ink);width:280px}
.brand-mark{width:34px;height:34px;background:var(--blue);border-radius:6px}
.head-divider{width:1px;height:80px;background:var(--line)}
.head-block{flex:1;padding-left:40px}
.head-label{font-size:22px;font-weight:600;margin-bottom:14px}
.head-value{font-size:14px;color:var(--muted)}
.swatches{display:flex;gap:10px}
.swatch{width:40px;height:40px;border-radius:50%}
.swatch-caption{display:flex;gap:10px;font-size:8px;color:var(--muted);margin-top:4px}
.swatch-caption span{width:40px;text-align:center}

/* screens */
.screen{position:absolute;left:240px;width:720px;height:540px;background:var(--white);border:1px solid var(--line);border-radius:10px;overflow:hidden;box-shadow:0 6px 24px rgba(30,40,60,.08)}
.screen-glow{position:absolute;right:0;bottom:0;width:360px;height:280px;background:radial-gradient(circle at 80% 80%,#eceef1 0%,rgba(255,255,255,0) 70%)}
.topbar{position:absolute;top:0;left:0;right:0;height:46px;display:flex;align-items:center;justify-content:space-between;padding:0 22px}
.topbar .brand{font-size:16px;gap:6px;width:auto}
.topbar .brand-mark{width:14px;height:14px;border-radius:3px}
.user-menu{display:flex;align-items:center;gap:10px;font-size:10px;font-weight:500}
.toggle{width:30px;height:16px;border-radius:8px;background:var(--blue);position:relative}
.toggle::after{content:"";position:absolute;right:2px;top:2px;width:12px;height:12px;border-radius:50%;background:var(--white)}
.crumb{position:absolute;top:56px;left:50%;transform:translateX(-50%);font-size:9px;color:var(--blue);border:1px solid #b9d9ef;border-radius:12px;padding:5px 16px;background:var(--white)}
.back{position:absolute;top:72px;left:26px;font-size:9px;color:var(--blue)}
.btn{display:inline-block;background:var(--blue);color:var(--white);font-size:9px;font-weight:600;border-radius:12px;padding:6px 18px}
.btn-small{font-size:7px;padding:4px 10px;border-radius:8px;background:var(--blue-soft);color:var(--blue);border:1px solid #b9d9ef}
.center-btn{position:absolute;left:50%;transform:translateX(-50%)}
.photo{background:linear-gradient(135deg,#c9b8a6,#8d9fb0);border-radius:4px}
.avatar{border-radius:50%;background:linear-gradient(135deg,#b8a18c,#6f8191)}

/* screen 1 */
.dash{position:absolute;top:96px;left:26px;right:26px;height:140px;border:1px solid var(--line);border-radius:6px;display:flex;background:var(--white)}
.dash-panel{padding:14px 18px;flex:1.7}
.dash-panel+.dash-panel{flex:1;border-left:1px solid var(--line)}
.panel-title{font-size:10px;font-weight:600;margin-bottom:12px}
.coach{display:flex;gap:14px;align-items:center}
.coach .avatar{width:54px;height:54px}
.link{font-size:8px;color:var(--blue);font-weight:500}
.fine{font-size:7px;color:var(--muted);line-height:1.5}
.member{display:flex;align-items:center;gap:8px;margin-bottom:8px}
.member .avatar{width:18px;height:18px}
.member .link{flex:1}
.tick{width:10px;height:10px}

/* screen 2 */
.events{position:absolute;top:96px;left:26px;right:26px;display:grid;grid-template-columns:1fr 1fr;gap:10px 14px}
.event{display:flex;gap:10px;border:1px solid var(--line);border-radius:6px;padding:6px;height:66px;background:var(--white)}
.event .photo{width:84px;flex:none}
.event h4{font-size:8px;font-weight:600;margin-bottom:3px}
.event .fine{font-size:6px;line-height:1.4;margin-bottom:4px}

/* screen 3 */
.question{position:absolute;top:98px;left:26px;font-size:9px;font-weight:600}
.textarea{border:1px solid var(--line);border-radius:6px;background:var(--white);font-size:8px;color:var(--muted);padding:8px}
.journal{position:absolute;top:114px;left:26px;width:440px;height:200px}
.tags{position:absolute;top:114px;left:486px;right:26px;display:grid;grid-template-columns:1fr 1fr;gap:8px}
.tag{font-size:7px;text-align:center;color:var(--blue);border:1px solid #b9d9ef;border-radius:4px;padding:6px 2px;background:var(--white)}

/* screen 4 */
.section-title{position:absolute;left:26px;font-size:10px;font-weight:600}
.obs-lines{position:absolute;top:116px;left:26px;width:560px}
.obs-lines p{font-size:7px;color:var(--muted);line-height:1.9}
.radios{position:absolute;top:116px;left:640px;display:flex;flex-direction:column;gap:6px}
.radio{width:12px;height:12px;border-radius:50%;border:1.5px solid var(--blue)}
.radio.on{background:var(--blue)}
.other{position:absolute;top:210px;left:26px;right:26px;height:62px}
.chips-label{position:absolute;top:296px;left:26px;font-size:7px;color:var(--blue)}
.chips{position:absolute;top:310px;left:26px;right:26px;display:flex;gap:8px}
.chips .tag{flex:1}
.chips .tag.on{background:var(--blue-soft)}

/* screen 5 */
.metrics{position:absolute;top:98px;left:26px;right:26px;display:grid;grid-template-columns:1fr 1fr;gap:14px 16px}
.metric{display:flex;border:1px solid var(--line);border-radius:6px;height:80px;background:var(--white)}
.metric.active{border-color:var(--blue)}
.metric p{flex:1;padding:10px 12px;font-size:7px;line-height:1.6;color:var(--ink)}
.metric.active p{color:var(--blue)}
.stepper{width:34px;border-left:1px solid var(--line);display:flex;flex-direction:column;align-items:center;justify-content:space-between;padding:8px 0;font-size:11px;color:var(--blue);font-weight:600}
.stepper .count{font-size:8px;color:var(--ink)}
</style>
</head>
<body>

<header class="sheet-head">
  <div class="brand"><span class="brand-mark"></span>Teamlens</div>
  <div class="head-divider"></div>
  <div class="head-block">
    <div class="head-label">Fonts:</div>
    <div class="head-value">Inter</div>
  </div>
  <div class="head-divider"></div>
  <div class="head-block">
    <div class="head-label">Colors:</div>
    <div class="swatches"><span class="swatch" style="background:var(--blue)"></span><span class="swatch" style="background:var(--blue-soft);border:1px solid var(--line)"></span></div>
    <div class="swatch-caption"><span>#3B9AD9</span><span>#E6F1FA</span></div>
  </div>
</header>

<!-- Home -->
<section class="screen" style="top:260px">
  <div class="screen-glow"></div>
  <div class="topbar"><div class="brand"><span class="brand-mark"></span>Teamlens</div><div class="user-menu">Professor ▾<span class="toggle"></span></div></div>
  <div class="crumb">Project Dashboard</div>
  <div class="dash">
    <div class="dash-panel">
      <div class="panel-title">Coaching</div>
      <div class="coach">
        <div class="avatar" role="img" aria-label="Coach profile photo"></div>
        <div><div class="link">Your coach today</div><div class="fine">Next session scheduled<br>Group work review</div></div>
      </div>
    </div>
    <div class="dash-panel">
      <div class="panel-title">My Team</div>
      <div class="member"><span class="avatar" role="img" aria-label="Team member photo"></span><span class="link">Team member one</span><svg class="tick" viewBox="0 0 10 10"><path d="M1 5l3 3 5-6" fill="none" stroke="#3b9ad9" stroke-width="1.5"/></svg></div>
      <div class="member"><span class="avatar" role="img" aria-label="Team member photo"></span><span class="link">Team member two</span><svg class="tick" viewBox="0 0 10 10"><path d="M1 5l3 3 5-6" fill="none" stroke="#3b9ad9" stroke-width="1.5"/></svg></div>
      <div class="fine">View all members</div>
    </div>
  </div>
</section>

<!-- Events -->
<section class="screen" style="top:900px">
  <div class="screen-glow"></div>
  <div class="topbar"><div class="brand"><span class="brand-mark"></span>Teamlens</div><div class="user-menu">Professor ▾<span class="toggle"></span></div></div>
  <div class="crumb">Events · Date Session</div>
  <div class="back">‹ Previous</div>
  <div class="events" style="top:104px">
    <div class="event"><div class="photo" role="img" aria-label="Event photo of a group at work"></div><div><h4>Event 1</h4><div class="fine">Biology class group work session with observations recorded.</div><span class="btn-small">Open Event</span></div></div>
    <div class="event"><div class="photo" role="img" aria-label="Event photo of a group at work"></div><div><h4>Event 2</h4><div class="fine">Math class group work session with observations recorded.</div><span class="btn-small">Open Event</span></div></div>
    <div class="event"><div class="photo" role="img" aria-label="Event photo of a group at work"></div><div><h4>Event 3</h4><div class="fine">Physics class group work session with observations recorded.</div><span class="btn-small">Open Event</span></div></div>
    <div class="event"><div class="photo" role="img" aria-label="Event photo of a group at work"></div><div><h4>Event 4</h4><div class="fine">Team planning session with notes and observations recorded.</div><span class="btn-small">Open Event</span></div></div>
    <div class="event"><div class="photo" role="img" aria-label="Event photo of a group at work"></div><div><h4>Event 5</h4><div class="fine">Project review session with notes and observations recorded.</div><span class="btn-small">Open Event</span></div></div>
    <div class="event"><div class="photo" role="img" aria-label="Event photo of a group at work"></div><div><h4>Event 6</h4><div class="fine">Closing workshop session with notes and observations recorded.</div><span class="btn-small">Open Event</span></div></div>
  </div>
  <span class="btn center-btn" style="top:340px">Next</span>
</section>

<!-- Journaling -->
<section class="screen" style="top:1568px">
  <div class="screen-glow"></div>
  <div class="topbar"><div class="brand"><span class="brand-mark"></span>Teamlens</div><div class="user-menu">Professor ▾<span class="toggle"></span></div></div>
  <div class="crumb">Event 1 · Date Session</div>
  <div class="back">‹ Previous</div>
  <div class="question" style="top:108px">Describe the current state of your team activities</div>
  <div class="textarea journal" style="top:124px">Write your notes here…</div>
  <div class="tags" style="top:124px">
    <span class="tag">Collaboration</span><span class="tag">Communication</span>
    <span class="tag">Social Interaction</span><span class="tag">Leadership</span>
    <span class="tag">Time Management</span><span class="tag">Conflict</span>
    <span class="tag">Participation</span><span class="tag">Focus</span>
    <span class="tag">Decision Making</span><span class="tag">Creativity</span>
  </div>
  <span class="btn center-btn" style="top:350px">Save Observation</span>
</section>

<!-- Observation -->
<section class="screen" style="top:2228px">
  <div class="screen-glow"></div>
  <div class="topbar"><div class="brand"><span class="brand-mark"></span>Teamlens</div><div class="user-menu">Professor ▾<span class="toggle"></span></div></div>
  <div class="crumb">Event 1 · Date Session</div>
  <div class="back">‹ Previous</div>
  <div class="section-title" style="top:100px">Observation</div>
  <div class="obs-lines">
    <p>The teenager directs other colleagues and keeps the group focused on the shared task goal.</p>
    <p>The teenager speaks more than everyone else during the discussion and planning phase.</p>
    <p>The teenager interrupts colleagues while they are speaking about their own ideas.</p>
    <p>The teenager listens carefully and builds on the ideas shared by the rest of the group.</p>
  </div>
  <div class="radios"><span class="radio"></span><span class="radio on"></span><span class="radio"></span></div>
  <div class="section-title" style="top:192px">Other Observation</div>
  <div class="textarea other">Add a note…</div>
  <div class="chips-label">Select category</div>
  <div class="chips">
    <span class="tag on">Collaboration</span><span class="tag">Communication</span><span class="tag">Leadership</span><span class="tag">Social Interaction</span><span class="tag">Participation</span><span class="tag">Focus</span>
  </div>
  <span class="btn center-btn" style="top:360px">Next</span>
</section>

<!-- Observations list -->
<section class="screen" style="top:2880px">
  <div class="screen-glow"></div>
  <div class="topbar"><div class="brand"><span class="brand-mark"></span>Teamlens</div><div class="user-menu">Professor ▾<span class="toggle"></span></div></div>
  <div class="crumb">Observations · Category 01</div>
  <div class="back">‹ Previous</div>
  <div class="metrics" style="top:108px">
    <div class="metric"><p>The teenager directs other colleagues and keeps the group focused on the shared task.</p><div class="stepper">+<span class="count">0</span>−</div></div>
    <div class="metric active"><p>The teenager speaks more than everyone else during the discussion and planning phase.</p><div class="stepper">+<span class="count">2</span>−</div></div>
    <div class="metric"><p>The teenager interrupts colleagues while they are speaking about their own ideas.</p><div class="stepper">+<span class="count">1</span>−</div></div>
    <div class="metric"><p>The teenager listens carefully and builds on the ideas shared by the rest of the group.</p><div class="stepper">+<span class="count">0</span>−</div></div>
    <div class="metric"><p>The teenager asks questions to clarify the task and checks everyone understands it.</p><div class="stepper">+<span class="count">0</span>−</div></div>
    <div class="metric"><p>The teenager shares materials and helps colleagues who are falling behind the group.</p><div class="stepper">+<span class="count">0</span>−</div></div>
    <div class="metric"><p>The teenager proposes a plan and assigns roles before the group starts working.</p><div class="stepper">+<span class="count">1</span>−</div></div>
    <div class="metric"><p>The work took the group this long from start to the final shared result.</p><div class="stepper">+<span class="count">00:25</span>−</div></div>
  </div>
</section>

</body>
</html>
```